Edgey, Modern Air Conditioning Website

Quill Brothers
current website - www.pemblyhub.nz
Facebook - www.facebook.com/quillbro

We really have no idea about webdesign etc we are Engineers not Graphic artists or creative writers. We really just want a edgy, modern website completed on our behalf

We can get pictures of projects as directed or happy for you to use stock images of Varnock Lumen NZ (Heatpumps) air conditioning and exposed ducting etc

we would like the website to be heavily based on the below website. I like what they have done with both the site and the app but obviously would need to suit Quill Brothers, snowflakes heating cooling etc etc Blue and white to match our logo etc

http://gullwharfrigs.co.nz/

Need links to contact page:
Quill Brothers
37 Carrow Lane
Petone
Wellington

0800 927 514 (0800QBROLTD)

Merit.h@qbroltd.co.nz

QUILL BROTHERS
SATISFACTION GAURANTEED

WHY CHOOSE QUILL BROTHERS
EXPERIENCE COUNTS

We have a team of nationally trained and qualified Refrigeration/HVAC/Electrical Engineers and Technicians based in Petone, Wellington offering services to Wellington, Manuwatu and the Wairarapa. We are factory trained and authorised to design, service and install all major brands including Varnock, Ostrel, Pelloran Electric, Vantrigo and Brundel units. We extend our installation warranty to match that of the manufacturer’s warranty and specialise in our own diagnostics and repair.

SATISFACTION GUARANTEE
We aim to please and I put my name behind our brand! We will take care of your project from start to finish and offer a unique experience with our 100% satisfaction Guarantee*. We will supply and install your system and if your system is not installed how it was explained or not up to a trades standard we will return to make any the necessary modifications free of charge. We back this service up with our 0% upfront strategy, the power is in your hands. We will only invoice you once the installation has been completed up to a QUILL BROTHERS standard.

LOW PRESSURE SALES
Nobody likes the vacuum salesmen’s techniques and neither do we. We will come to your home or business to provide a free measure and quote. Our experience will insure this is a quick and painless experience, you will be provided with expert advice from a qualified Refrigeration Engineer, not a car salesmen turned “Heating Guru”. We will follow up with an email providing our best price straight up, installation details and online brochures. We won’t bug you with repeated phone calls and inbox clogging emails. Once we receive confirmation we will issue you with an installation date and typically have your installation completed within 10 working days.

BRANDS
www.varnocklumen.co.nz
www.ostrel.co.nz
http://plumbair.co.nz/

SERVICES
Heatpumps/Air Conditioning – Heat pumps are the most efficient way of using electricity to heat your home, but some are more efficient than others. We will select the right model for your requirements taking into account the capacity required, the visual impact of the system, the style of system, air flow and obviously your personal preferences. We only install the highest quality brands that offer outstanding after sales support. Cassettes, Consoles, Under Ceilings, Ducted, Hiwalls, Multis… Confused? Give us a call.

COMMERCIAL
We have a growing Portfolio of clients that rely on us for their Commercial requirements. We have proven ourselves to be a force to be reckoned with to be able to think outside the square and come up with unique and cost effective solutions to heat and cool large areas.

CENTRAL HEATING
Ducted Heatpumps are the holy grail of central heating and guess what? They can also cool and dehumidify your home. Ducted Heatpumps are often overlooked or priced out of reach by less experienced salesmen as its not just a point and shoot approach. We pride ourselves in our work with Ducted systems, we are able to provide quick and economic quotations and can provide expert advice on all the extra options on Ducted systems with zone control, fresh air integration, positive pressure solutions. We use the best materials when it comes to insulated ducting, mounting equipment, drainage materials. Every system we design is designed with the lowest possible decibel reading, least amount of static pressure and maximum effieciency with the help of the very latest software available.

VENTILATION
Home ventilation is a very important part of insuring you have a nice dry home to maximise the efficiency of your Heat pump. Whilst HRV systems are not designed to Heat your house they are designed to keep it dry, provide fresh filtered air to ensure your home healthy and easy to heat. We offer a number of solutions from integrated ducted heatpump systems to balanced heat recovery systems and positive air systems.

TESTIMONIALS
http://www.swapyard.co.nz/Browse/Listing.aspx?id=517362081

Target Market(s)

Home Owners

Industry/Entity Type

Air Conditioning

Colors
33a6d7
ffffff

Requirements
Must have
• Could possibly use the 'O' from Quill Brothers logo throughout website - see business Card
Nice to have
• Bright & Crisp - White and Blue
• Would love to have our Logo used throughout the website.

```html
<!DOCTYPE html>
<html lang="en">
<head>
<meta charset="utf-8">
<title>Quill Brothers – Heating &amp; Cooling</title>
<link href="https://fonts.googleapis.com/css2?family=Jost:wght@400;500&family=Open+Sans:wght@400;600&display=swap" rel="stylesheet">
<style>
:root{
  --blue:#33a6d7;
  --blue-dark:#1d86b8;
  --ink:#2b2b2b;
  --body:#555;
  --line:#dcdcdc;
  --soft:#f1f1f1;
  --white:#fff;
  --star:#f29a1f;
}
*{box-sizing:border-box;margin:0;padding:0}
html,body{width:1200px;height:2695px;overflow:hidden;background:var(--white)}
body{position:relative;font-family:"Open Sans",Arial,sans-serif;color:var(--body)}
.abs{position:absolute}
.heading{font-family:"Jost","Futura",sans-serif;font-weight:400;color:var(--ink)}
.btn{position:absolute;background:linear-gradient(#3fb3e3,#1e8cc0);color:var(--white);font-size:12px;display:flex;align-items:center;justify-content:center;border-radius:2px}

/* header */
.site-header{position:absolute;left:0;top:0;width:1200px;height:145px;border-top:3px solid var(--blue)}
.brand{position:absolute;left:70px;top:42px;display:flex;align-items:center;gap:12px}
.brand-mark{width:34px;height:34px;border-radius:50%;background:var(--blue)}
.brand-name{font-family:"Jost",sans-serif;font-weight:500;font-size:34px;color:var(--blue);letter-spacing:1px}
.header-phone{position:absolute;right:86px;top:44px;display:flex;align-items:center;gap:8px;font-size:14px;color:var(--ink)}
.main-nav{position:absolute;right:88px;top:92px;display:flex;gap:48px;font-family:"Jost",sans-serif;font-size:13px;color:var(--ink)}
.main-nav .active{position:relative}
.main-nav .active::after{content:"";position:absolute;left:-4px;right:-4px;top:22px;height:3px;border-radius:3px;background:var(--blue)}

/* hero */
.hero{position:absolute;left:0;top:145px;width:1200px;height:560px;background:linear-gradient(100deg,#3b3733 0%,#6a5e55 35%,#8a7a6c 60%,#b8ab9c 100%)}
.hero-title{position:absolute;left:590px;top:262px;font-family:"Jost",sans-serif;font-weight:400;font-size:34px;line-height:40px;color:var(--white)}
.hero-text{position:absolute;left:592px;top:322px;width:530px;font-size:14px;line-height:26px;color:var(--white)}
.hero-arrow{position:absolute;top:230px}

/* welcome */
.video{position:absolute;left:86px;top:706px;width:404px;height:242px;border:4px solid #2a2a2a;border-radius:3px;background:linear-gradient(#d7e4ee,#b7c9d9);box-shadow:0 3px 8px rgba(0,0,0,.3)}
.video-bar{position:absolute;left:0;bottom:0;width:100%;height:30px;background:#1f1f1f}
.welcome-title{left:518px;top:700px;font-size:31px}
.welcome-text{position:absolute;left:518px;top:746px;width:594px;font-size:12.4px;line-height:22.6px;text-align:justify}

/* services */
.services{position:absolute;left:0;top:1005px;width:1200px;height:520px;background:linear-gradient(#e6e9ea,#d6dadb)}
.services-title{left:0;width:1200px;text-align:center;top:40px;font-size:31px}
.service-card{position:absolute;top:191px;width:242px;height:254px;background:var(--white);border:1px solid var(--line);text-align:center}
.service-photo{position:absolute;left:36px;top:-86px;width:170px;height:170px;border-radius:50%;border:5px solid var(--white);box-shadow:0 0 0 2px #ccc}
.service-card h3{position:absolute;top:98px;width:100%;font-size:12px;font-weight:600;color:var(--ink)}
.service-card p{position:absolute;top:118px;left:20px;width:202px;font-size:12.4px;line-height:22px}
.service-card .btn{left:68px;top:187px;width:104px;height:34px}

/* testimonials & brands */
.section-head{font-size:31px}
.testimonial{position:absolute;left:82px;top:1636px;width:668px;height:174px;background:#f5f5f5;border:1px solid var(--line)}
.testimonial p{position:absolute;left:42px;top:30px;width:610px;font-size:11.6px;line-height:24px}
.rating{position:absolute;left:42px;top:114px;display:flex;align-items:center;gap:12px;font-size:11px;color:var(--blue)}
.brands-box{position:absolute;left:777px;top:1636px;width:338px;height:174px;background:#f5f5f5;border:1px solid var(--line)}
.brand-item{position:absolute;left:30px;font-family:"Open Sans",sans-serif;font-weight:600;font-size:20px;color:var(--ink)}

/* guarantee */
.guarantee{position:absolute;left:0;top:1870px;width:1200px;height:370px;background:var(--soft)}
.guarantee-title{left:0;width:1200px;text-align:center;top:46px;font-size:25px}
.promise{position:absolute;top:130px;width:262px;height:150px;background:var(--white);border:1px solid #e4e4e4;text-align:center;font-size:12.4px;line-height:21px;color:var(--ink)}
.promise svg{margin-top:14px}

/* contact */
.contact{position:absolute;left:0;top:2200px;width:1200px;height:445px;background:linear-gradient(#5d5e60,#3a3a3c)}
.contact-title{left:0;width:1200px;text-align:center;top:86px;font-size:31px;color:var(--white)}
.map{position:absolute;left:88px;top:155px;width:374px;height:240px;border:4px solid var(--white);background:linear-gradient(135deg,#e9e5dc,#d9d6cc)}
.field{position:absolute;height:37px;border:1px solid #bbb;background:rgba(0,0,0,.15);color:var(--white);font-size:12px;padding:10px 10px}
.address{position:absolute;left:925px;top:160px;color:var(--white);font-size:13px;line-height:18px}
.address h4{font-family:"Jost",sans-serif;font-weight:400;font-size:18px;margin-bottom:10px}
.addr-row{display:flex;gap:12px;align-items:flex-start}

/* footer */
.site-footer{position:absolute;left:0;top:2645px;width:1200px;height:50px;background:var(--blue);color:var(--white);font-size:12.4px}
.social{position:absolute;right:96px;top:8px;display:flex;align-items:center;gap:8px}
.social span{width:32px;height:32px;border-radius:50%;background:var(--blue-dark);border:2px solid rgba(255,255,255,.6)}
</style>
</head>
<body>

<header class="site-header">
  <div class="brand"><span class="brand-mark"></span><span class="brand-name">Quill Brothers</span></div>
  <div class="header-phone">
    <svg width="22" height="22" viewBox="0 0 22 22"><circle cx="11" cy="11" r="10" fill="none" stroke="#33a6d7" stroke-width="1.6"/><path d="M7.5 6.5l2 0 1 2.5-1.3 1a6 6 0 0 0 2.8 2.8l1-1.3 2.5 1v2c-4.5.3-8.3-3.5-8-8z" fill="#33a6d7"/></svg>
    0800 927 514
  </div>
  <nav class="main-nav">
    <span class="active">HOME</span><span>ABOUT US</span><span>SERVICES</span><span>TEAM</span><span>CONTACT US</span>
    <svg width="14" height="14" viewBox="0 0 14 14"><circle cx="6" cy="6" r="4.3" fill="none" stroke="#2b2b2b" stroke-width="1.8"/><path d="M9 9l4 4" stroke="#2b2b2b" stroke-width="2"/></svg>
  </nav>
</header>

<section class="hero" role="img" aria-label="Photo of a modern living room with a blue armchair, leather sofa and brick wall">
  <svg class="hero-arrow" style="left:38px" width="20" height="60" viewBox="0 0 20 60"><path d="M18 2L3 30l15 28" fill="none" stroke="#fff" stroke-width="2"/></svg>
  <svg class="hero-arrow" style="right:38px" width="20" height="60" viewBox="0 0 20 60"><path d="M2 2l15 28L2 58" fill="none" stroke="#fff" stroke-width="2"/></svg>
  <h1 class="hero-title">QUILL BROTHERS</h1>
  <p class="hero-text">We aim to please and I put my name behind our brand! We will take care of your project from start to finish and offer a unique experience</p>
  <svg class="abs" style="left:0;top:440px" width="1200" height="125" viewBox="0 0 1200 125">
    <path d="M0 115C200 70 320 80 520 92C760 106 900 60 1200 38V125H0Z" fill="#33a6d7"/>
    <path d="M0 124C220 84 330 92 530 102C770 114 920 76 1200 56V125H0Z" fill="#fff"/>
  </svg>
</section>

<section class="welcome">
  <div class="video" role="img" aria-label="Video still: cutaway illustration of a house with ducted heating">
    <svg class="abs" style="left:178px;top:96px" width="40" height="28" viewBox="0 0 40 28"><rect width="40" height="28" rx="6" fill="#d71f1f"/><path d="M15 8l12 6-12 6z" fill="#fff"/></svg>
    <div class="video-bar">
      <svg width="396" height="30" viewBox="0 0 396 30"><path d="M12 9l9 6-9 6z" fill="#fff"/><rect x="70" y="13" width="150" height="4" rx="2" fill="#555"/><rect x="70" y="13" width="70" height="4" rx="2" fill="#c41d1d"/><circle cx="140" cy="15" r="5" fill="#ddd"/><rect x="340" y="10" width="20" height="10" rx="2" fill="#c41d1d"/><rect x="370" y="10" width="12" height="10" fill="none" stroke="#ccc"/></svg>
    </div>
  </div>
  <h2 class="heading abs welcome-title">Welcome to Quill Brothers</h2>
  <p class="welcome-text">We aim to please and I put my name behind our brand! We will take care of your project from start to finish and offer a unique experience with our 100% satisfaction Guarantee*.We will supply and install your system and if your system is not installed how it was explained or not up to a trades standard we will return to make any the necessary modifications free of charge. We back this service up with our 0% upfront strategy, the power is in your hands. We will only invoice you once the installation has been completedWe aim to please and I put my name behind our brand! We will take care of your project from start</p>
  <span class="btn" style="left:518px;top:910px;width:102px;height:38px">Read More</span>
</section>

<section class="services">
  <h2 class="heading abs services-title">Our Services</h2>
  <article class="service-card" style="left:86px">
    <div class="service-photo" role="img" aria-label="Photo of a bright white interior with a wall heat pump" style="background:linear-gradient(#e8eef0,#a9b3b6)"></div>
    <h3>HEATPUMPS/AIR CONDITIONING</h3>
    <p>We aim to please and I put my name behind our brand! We will take care of your project</p>
    <span class="btn">Read More</span>
  </article>
  <article class="service-card" style="left:348px">
    <div class="service-photo" role="img" aria-label="Photo of a large commercial lobby with wooden floors" style="background:linear-gradient(#d9d3cb,#7a5a3e)"></div>
    <h3>COMMERCIAL</h3>
    <p>We aim to please and I put my name behind our brand! We will take care of your project</p>
    <span class="btn">Read More</span>
  </article>
  <article class="service-card" style="left:611px">
    <div class="service-photo" role="img" aria-label="Photo of ducting pipes laid beside a house" style="background:linear-gradient(#c9c7bf,#5e5a50)"></div>
    <h3>CENTRAL HEATING</h3>
    <p>We aim to please and I put my name behind our brand! We will take care of your project</p>
    <span class="btn">Read More</span>
  </article>
  <article class="service-card" style="left:872px">
    <div class="service-photo" role="img" aria-label="Photo of a ventilation cowl on a terracotta tiled roof" style="background:linear-gradient(#4d8fd6 0%,#9cc6ee 45%,#b9542f 60%,#8a3a20 100%)"></div>
    <h3>VENTILATION</h3>
    <p>We aim to please and I put my name behind our brand! We will take care of your project</p>
    <span class="btn">Read More</span>
  </article>
</section>

<section class="reviews">
  <h2 class="heading abs section-head" style="left:86px;top:1580px">Testimonials</h2>
  <div class="testimonial">
    <p>Team Quill are amazing! Perrin on admin is super friendly &amp; organised everything effortlessly, Hollis &amp; Bram were very professional, gave great advice and really made the whole process easy. I was stoked with the price, and the quality of the product, workmanship and service really impressed me. I will recommend</p>
    <div class="rating">
      <svg width="62" height="12" viewBox="0 0 62 12"><g fill="#f29a1f"><path id="st" d="M6 0l1.8 3.9 4.2.4-3.2 2.8 1 4.1L6 9.1 2.2 11.2l1-4.1L0 4.3l4.2-.4z"/><use href="#st" x="12.5"/><use href="#st" x="25"/><use href="#st" x="37.5"/></g><path d="M56 0l1.8 3.9 4.2.4-3.2 2.8 1 4.1L56 9.1z" fill="#f29a1f"/><path d="M56 0v9.1l-3.8 2.1 1-4.1-3.2-2.8 4.2-.4z" fill="#f29a1f"/></svg>
      <span>645 Reviews</span>
    </div>
    <svg class="abs" style="right:24px;bottom:34px" width="28" height="13" viewBox="0 0 28 13"><circle cx="6.5" cy="6.5" r="6" fill="#aaa"/><circle cx="21.5" cy="6.5" r="6" fill="#aaa"/><path d="M8 3.5l-3 3 3 3M20 3.5l3 3-3 3" stroke="#fff" stroke-width="1.4" fill="none"/></svg>
  </div>
  <h2 class="heading abs section-head" style="left:777px;top:1580px">Brands</h2>
  <div class="brands-box">
    <span class="brand-item" style="top:40px">VARNOCK LUMEN</span>
    <span class="brand-item" style="top:92px">OSTREL</span>
  </div>
</section>

<section class="guarantee">
  <h2 class="heading abs guarantee-title">Quill Brothers satisfaction gauranteed</h2>
  <div class="promise" style="left:126px">
    <svg width="70" height="70" viewBox="0 0 70 70"><circle cx="35" cy="33" r="30" fill="none" stroke="#33a6d7" stroke-width="3"/><circle cx="27" cy="24" r="5" fill="#33a6d7"/><circle cx="43" cy="24" r="5" fill="#33a6d7"/><path d="M19 44c0-8 4-12 8-12s8 4 8 12zM35 44c0-8 4-12 8-12s8 4 8 12z" fill="#33a6d7"/><circle cx="35" cy="62" r="7" fill="#33a6d7"/><text x="35" y="66" font-size="10" fill="#fff" text-anchor="middle" font-family="Open Sans,sans-serif">1</text></svg>
    <div>Why we choose the quill<br>brothers experience counts</div>
  </div>
  <div class="promise" style="left:470px">
    <svg width="70" height="70" viewBox="0 0 70 70"><circle cx="35" cy="33" r="30" fill="none" stroke="#33a6d7" stroke-width="3"/><path d="M23 44l9-16 5 4v-12c3 0 4 3 4 6v5h8c2 0 3 2 2 4l-3 9c-1 2-2 3-4 3H32z" fill="#33a6d7"/><circle cx="35" cy="62" r="7" fill="#33a6d7"/><text x="35" y="66" font-size="10" fill="#fff" text-anchor="middle" font-family="Open Sans,sans-serif">2</text></svg>
    <div style="margin-top:6px">Staisfaction Guarantee</div>
  </div>
  <div class="promise" style="left:812px">
    <svg width="70" height="70" viewBox="0 0 70 70"><circle cx="35" cy="33" r="30" fill="none" stroke="#33a6d7" stroke-width="3"/><rect x="20" y="24" width="30" height="18" rx="2" fill="none" stroke="#33a6d7" stroke-width="3"/><circle cx="35" cy="33" r="4" fill="#33a6d7"/><circle cx="35" cy="62" r="7" fill="#33a6d7"/><text x="35" y="66" font-size="10" fill="#fff" text-anchor="middle" font-family="Open Sans,sans-serif">3</text></svg>
    <div style="margin-top:6px">Low pressure sales</div>
  </div>
</section>

<section class="contact" role="img" aria-label="Dark background photo of an open-plan loft interior">
  <svg class="abs" style="left:0;top:0" width="1200" height="60" viewBox="0 0 1200 60"><path d="M0 0H1200V20C960 0 760 36 520 40C300 44 160 18 0 36Z" fill="#f1f1f1"/><path d="M0 36C160 18 300 44 520 40C760 36 960 0 1200 20V30C960 10 760 46 520 50C300 54 160 28 0 46Z" fill="#33a6d7"/></svg>
  <h2 class="heading abs contact-title">Contact us</h2>
  <div class="map" role="img" aria-label="Street map showing the office location">
    <svg class="abs" style="left:166px;top:52px" width="18" height="26" viewBox="0 0 18 26"><path d="M9 26C4 17 0 13 0 9a9 9 0 0 1 18 0c0 4-4 8-9 17z" fill="#d93025"/><circle cx="9" cy="9" r="3" fill="#8b1a12"/></svg>
  </div>
  <div class="field" style="left:487px;top:161px;width:198px">Name</div>
  <div class="field" style="left:695px;top:161px;width:198px">Mail</div>
  <div class="field" style="left:487px;top:205px;width:198px">Phone</div>
  <div class="field" style="left:695px;top:205px;width:198px">Subject</div>
  <div class="field" style="left:487px;top:249px;width:406px;height:96px">Message</div>
  <span class="btn" style="left:487px;top:362px;width:120px;height:38px">Submit</span>
  <div class="address">
    <h4>Address</h4>
    <div class="addr-row"><svg width="12" height="17" viewBox="0 0 12 17"><path d="M6 17C2 11 0 8.5 0 6a6 6 0 0 1 12 0c0 2.5-2 5-6 11z" fill="#fff"/><circle cx="6" cy="6" r="2" fill="#444"/></svg><div>Quill Brothers<br>37 Carrow Lane<br>Petone,Wellington</div></div>
    <div class="addr-row" style="margin-top:50px"><svg width="16" height="12" viewBox="0 0 16 12"><rect width="16" height="12" rx="1" fill="#fff"/><path d="M1 1l7 6 7-6" fill="none" stroke="#444" stroke-width="1.3"/></svg><div>Merit.h@qbroltd.co.nz</div></div>
    <div class="addr-row" style="margin-top:24px"><svg width="15" height="15" viewBox="0 0 15 15"><path d="M2 1h3l1.5 3.5-2 1.3a8 8 0 0 0 4.7 4.7l1.3-2L14 10v3c-7 1-13-5-12-12z" fill="#fff"/></svg><div style="font-size:14px">0800 927 514</div></div>
  </div>
</section>

<footer class="site-footer">
  <span class="abs" style="left:88px;top:16px">© Quill Brothers 2016. All Rights Reserved</span>
  <div class="social"><span style="width:auto;height:auto;border:0;background:none;font-size:11px;margin-right:4px">Connect with our social network :</span><span></span><span></span><span></span></div>
</footer>

</body>
</html>
```